4D Hush Little Nest Luxury Ultrasound Billboard

Design a HIGH-END, MODERN billboard for my private prenatal ultrasound studio, 4D Hush Little Nest, located in Pace, Florida.
This billboard will be viewed by drivers traveling at highway speeds, so it must be extremely clean, simple, and readable within 6 seconds.
About My Business
4D Hush Little Nest is a private prenatal ultrasound studio specializing in:
Highest technology 4D/HD Ultrasounds
Early Gender Determination
Pregnancy Confirmation
I have been serving families for nearly 10 years and is known for creating a memorable experience, not just an ultrasound appointment.
Design Style
I DO NOT want:
Flowers
Leaves
Swirls
Glitter
Hearts everywhere
Busy backgrounds
Generic maternity stock graphics
I DO want:
Modern
Luxury
Upscale
Clean
Professional
Eye-catching
Premium medical spa feel
Colors
Use colors from my logo:
LOGO Green ( or a deep green)
Black
White
Soft Gold accents
Images:
Incorporate my professional headshot in a clean, modern way, logo, and the ultrasound images
Text
Keep wording minimal.
Primary Headline ( OPEN TO IDEAS) :
EXAMPLES ( WOULD RATHER SOMETHING MORE CATCHY)
" ADVANCED IMAGING. UNFORGETTABLE MOMENTS"
"MEET YOUR BABY BEFORE BIRTH"
Under headline:
4D Ultrasound • Early Gender • Pregnancy Confirmation
Business Name:
4D Hush Little Nest
Private Prenatal Ultrasound Studio
Phone Number:
850-471-3905
Important
This billboard must be readable in 5–6 seconds from a moving vehicle.
Less text is better.
The phone number and business name must be visible from a distance.
The design should feel like a premium brand that immediately tells expecting parents:
“This is where I go to see my baby.”
Files Provided
Official logo
Headshot
Ultrasound images
Don’t make this look like a medical office billboard.
Make it look like a luxury baby experience billboard. That’s what separates 4D Hush Little Nest from hospitals, OB offices, and all the new studios popping up around you. The emotional connection is what gets moms to book. ❤️
Billboard Size - 10.6” x 36”

```html
<!DOCTYPE html>
<html lang="en">
<head>
<meta charset="utf-8">
<title>4D Hush Little Nest Billboard</title>
<link rel="stylesheet" href="https://fonts.googleapis.com/css2?family=Libre+Baskerville&family=Montserrat:wght@400;600&family=Roboto+Condensed:wght@700&family=Roboto:wght@700&display=swap">
<style>
  :root {
    --green: #5f7068;
    --gold: #c99a3a;
    --white: #ffffff;
    --frame: #3a3a3a;
    --photo-light: #eceae6;
    --photo-mid: #b9bdb6;
    --scrub: #4f6150;
    --scan-dark: #3a1410;
    --scan-warm: #b8776a;
  }
  html, body {
    margin: 0;
    width: 1200px;
    height: 407px;
    overflow: hidden;
    background: var(--white);
  }
  .canvas {
    position: relative;
    width: 1200px;
    height: 407px;
  }
  .billboard {
    position: absolute;
    left: 50px;
    top: 41px;
    width: 1107px;
    height: 327px;
    background: var(--white);
    border: 1px solid var(--frame);
    box-shadow: 1px 2px 3px rgba(0,0,0,0.35);
    overflow: hidden;
  }
  .headline {
    position: absolute;
    left: 32px;
    top: 8px;
    margin: 0;
    font-family: "Libre Baskerville", serif;
    font-weight: 400;
    font-size: 80px;
    line-height: 1;
    color: var(--green);
    white-space: nowrap;
    letter-spacing: 0.01em;
  }
  .subhead {
    position: absolute;
    left: 32px;
    top: 88px;
    margin: 0;
    font-family: "Montserrat", sans-serif;
    font-weight: 400;
    font-size: 56px;
    line-height: 1;
    color: var(--gold);
    letter-spacing: 0.19em;
    white-space: nowrap;
  }
  .rule {
    position: absolute;
    left: 32px;
    top: 152px;
    width: 563px;
    height: 2px;
    background: linear-gradient(90deg, var(--gold) 0%, var(--gold) 55%, rgba(201,154,58,0) 100%);
  }
  .services {
    position: absolute;
    left: 28px;
    top: 166px;
    margin: 0;
    padding: 0;
    list-style: none;
    font-family: "Roboto Condensed", sans-serif;
    font-weight: 700;
    font-size: 38px;
    line-height: 40px;
    color: var(--green);
    letter-spacing: 0.1em;
    white-space: nowrap;
  }
  .services .dot {
    color: var(--gold);
    margin-right: 10px;
  }
  .band {
    position: absolute;
    left: 0;
    top: 254px;
    width: 940px;
    height: 73px;
    background: linear-gradient(90deg, var(--green) 0%, var(--green) 80%, rgba(95,112,104,0) 100%);
  }
  .phone {
    position: absolute;
    left: 33px;
    top: 266px;
    width: 44px;
    height: 44px;
  }
  .phone-number {
    position: absolute;
    left: 92px;
    top: 254px;
    margin: 0;
    font-family: "Roboto", sans-serif;
    font-weight: 700;
    font-size: 68px;
    line-height: 1;
    color: var(--white);
    letter-spacing: 3px;
    white-space: nowrap;
  }
  .headshot {
    position: absolute;
    right: 0;
    top: 0;
    width: 300px;
    height: 327px;
    background:
      linear-gradient(90deg, var(--white) 0%, rgba(255,255,255,0) 25%),
      radial-gradient(ellipse 70px 150px at 190px 250px, var(--scrub) 0%, rgba(79,97,80,0) 100%),
      linear-gradient(180deg, var(--photo-light) 0%, var(--photo-mid) 100%);
  }
  .scan {
    position: absolute;
    left: 732px;
    top: 93px;
    width: 130px;
    height: 117px;
    border: 2px solid var(--green);
    border-radius: 14px;
    background: linear-gradient(160deg, var(--scan-warm) 0%, var(--scan-dark) 50%, var(--scan-warm) 100%);
  }
  .brand {
    position: absolute;
    left: 711px;
    top: 223px;
    width: 172px;
    height: 83px;
    border: 2px solid var(--green);
    border-radius: 12px;
    background: var(--white);
    text-align: center;
  }
  .brand-name {
    margin: 18px 0 0;
    font-family: "Montserrat", sans-serif;
    font-weight: 600;
    font-size: 15px;
    line-height: 1.2;
    color: var(--gold);
  }
  .brand-line {
    width: 146px;
    height: 1px;
    margin: 10px auto 6px;
    background: var(--gold);
  }
  .brand-tagline {
    margin: 0;
    font-family: "Montserrat", sans-serif;
    font-weight: 600;
    font-size: 7.5px;
    letter-spacing: 0.04em;
    color: var(--green);
  }
</style>
</head>
<body>
  <div class="canvas">
    <section class="billboard">
      <div class="headshot" role="img" aria-label="Professional headshot of the studio owner in green scrubs holding an ultrasound probe"></div>

      <h1 class="headline">MEET YOUR BABY</h1>
      <p class="subhead">BEFORE BIRTH</p>
      <div class="rule"></div>

      <ul class="services">
        <li><span class="dot">•</span>4D ULTRASOUND <span class="dot">•</span>EARLY GENDER</li>
        <li><span class="dot">•</span>PREGNANCY CONFIRMATION</li>
      </ul>

      <div class="band"></div>
      <svg class="phone" viewBox="0 0 44 44" aria-hidden="true">
        <circle cx="22" cy="22" r="20" fill="none" stroke="#ffffff" stroke-width="2.5"/>
        <path d="M15 12c1-1 2.5-1 3 0l2.5 4c.5 1 .2 2-.6 2.6l-1.4 1c1 2.6 3 4.6 5.6 5.8l1-1.4c.6-.8 1.7-1 2.6-.5l4 2.5c1 .6 1 2 0 3l-2 2c-1.2 1.2-3 1.5-4.6.8C19.5 29.8 14.4 24.6 12.2 19c-.6-1.6-.3-3.4.9-4.6z" fill="#ffffff"/>
      </svg>
      <p class="phone-number">850-471-3905</p>

      <div class="scan" role="img" aria-label="4D ultrasound image of a baby"></div>

      <div class="brand">
        <p class="brand-name">4D Hush Little Nest</p>
        <div class="brand-line"></div>
        <p class="brand-tagline">PRENATAL ULTRASOUND STUDIO</p>
      </div>
    </section>
  </div>
</body>
</html>
```